Letterhead and Envelope for Mental Health Business

I need letterhead and envelope designs that will match my business cards. I am attaching a *.pds file of my business card so it can be matched.

```html
<!DOCTYPE html>
<html lang="en">
<head>
<meta charset="utf-8">
<title>Hale Counseling Stationery</title>
<link href="https://fonts.googleapis.com/css2?family=Arimo:wght@400;700&display=swap" rel="stylesheet">
<style>
  :root {
    --navy: #1f4e80;
    --band: #24507f;
    --green: #5a8a2e;
    --paper: #f7f7f7;
    --paper-shade: #e4e4e4;
    --stage: #d9d6d2;
    --ink-light: #e8eef5;
    --ink-muted: #8a8f96;
    --mark: rgba(120,120,120,0.16);
  }
  * { box-sizing: border-box; margin: 0; padding: 0; }
  html, body { width: 1200px; height: 900px; overflow: hidden; }
  body {
    background: var(--stage);
    font-family: "Arimo", Arial, sans-serif;
    position: relative;
  }
  .sheet {
    position: absolute;
    background: linear-gradient(160deg, #ffffff 0%, var(--paper) 55%, var(--paper-shade) 100%);
    box-shadow: 0 8px 22px rgba(0,0,0,0.28);
    overflow: hidden;
  }
  .brand {
    display: flex; align-items: center; gap: 6px;
    position: absolute;
  }
  .brand-dot {
    border-radius: 50%;
    background: var(--green);
    flex: none;
  }
  .brand-name {
    color: var(--navy);
    font-weight: 700;
    line-height: 1;
    letter-spacing: 0.02em;
    text-transform: uppercase;
  }
  .band { position: absolute; left: 0; bottom: 0; width: 100%; }
  .band svg { display: block; width: 100%; height: 100%; }
  .mark {
    position: absolute;
    border-radius: 50%;
    border: 22px solid var(--mark);
  }
  .band-text {
    position: absolute;
    color: var(--ink-light);
    letter-spacing: 0.08em;
    line-height: 1.55;
  }

  /* letterhead */
  .letterhead { left: 610px; top: 100px; width: 470px; height: 680px; }
  .letterhead .brand { left: 50%; top: 48px; transform: translateX(-50%); }
  .letterhead .brand-dot { width: 30px; height: 30px; }
  .letterhead .brand-name { font-size: 19px; }
  .letterhead .mark { width: 260px; height: 260px; right: -20px; bottom: 110px; }
  .letterhead .band { height: 150px; }
  .letterhead .band-left { left: 36px; bottom: 22px; font-size: 10px; }
  .letterhead .band-right { right: 26px; bottom: 68px; font-size: 10px; text-align: right; }

  /* envelope */
  .envelope { left: 90px; top: 560px; width: 530px; height: 275px; }
  .envelope .brand { left: 34px; top: 34px; }
  .envelope .brand-dot { width: 24px; height: 24px; }
  .envelope .brand-name { font-size: 15px; }
  .envelope .mark { width: 150px; height: 150px; right: 30px; top: 70px; border-width: 14px; }
  .envelope .band { height: 100px; }
  .envelope .band-left { left: 30px; bottom: 14px; font-size: 7.5px; }
  .envelope .band-right { right: 18px; bottom: 58px; font-size: 7.5px; text-align: right; }

  /* business card */
  .card { left: 210px; top: 320px; width: 200px; height: 130px; }
  .card .brand { left: 50%; top: 14px; transform: translateX(-50%); }
  .card .brand-dot { width: 18px; height: 18px; }
  .card .brand-name { font-size: 12px; }
  .card .holder {
    position: absolute; top: 40px; width: 100%; text-align: center;
    color: var(--navy); font-size: 11px; font-weight: 700; letter-spacing: 0.05em;
  }
  .card .credentials {
    position: absolute; top: 55px; width: 100%; text-align: center;
    color: var(--ink-muted); font-size: 5.5px; letter-spacing: 0.1em;
  }
  .card .band { height: 62px; }
  .contact-list {
    position: absolute; left: 12px; bottom: 7px; list-style: none;
    font-size: 6px; color: var(--ink-light); letter-spacing: 0.04em; line-height: 1.55;
  }
  .contact-list span { display: inline-block; width: 22px; color: #9fb3c8; font-size: 4.5px; }
</style>
</head>
<body>

<section class="sheet letterhead" aria-label="Letterhead">
  <div class="brand"><span class="brand-dot"></span><span class="brand-name">Hale Counseling</span></div>
  <div class="mark" aria-hidden="true"></div>
  <div class="band">
    <svg viewBox="0 0 470 150" preserveAspectRatio="none" aria-hidden="true">
      <path d="M0,20 Q250,55 470,-6 L470,6 Q260,68 0,36 Z" fill="var(--green)"/>
      <path d="M0,41 Q260,74 470,11 L470,150 L0,150 Z" fill="var(--band)"/>
    </svg>
  </div>
  <p class="band-text band-left">555/014-2290<br>Elm Street 45, 1020 Springfield, USA</p>
  <p class="band-text band-right">daniel@halecounselingllc.com<br>www.halecounselingllc.com</p>
</section>

<section class="sheet envelope" aria-label="Envelope">
  <div class="brand"><span class="brand-dot"></span><span class="brand-name">Hale Counseling</span></div>
  <div class="mark" aria-hidden="true"></div>
  <div class="band">
    <svg viewBox="0 0 530 100" preserveAspectRatio="none" aria-hidden="true">
      <path d="M0,14 Q300,40 530,-4 L530,6 Q300,50 0,25 Z" fill="var(--green)"/>
      <path d="M0,29 Q300,55 530,10 L530,100 L0,100 Z" fill="var(--band)"/>
    </svg>
  </div>
  <p class="band-text band-right">www.halecounselingllc.com</p>
  <p class="band-text band-left">555/014-2290<br>Elm Street 45, 1020 Springfield, USA</p>
</section>

<section class="sheet card" aria-label="Business card">
  <div class="brand"><span class="brand-dot"></span><span class="brand-name">Hale Counseling</span></div>
  <p class="holder">Daniel Hale</p>
  <p class="credentials">LMHC, NCC, DCC</p>
  <div class="band">
    <svg viewBox="0 0 200 62" preserveAspectRatio="none" aria-hidden="true">
      <path d="M0,4 L200,4 L200,62 L0,62 Z" fill="var(--band)"/>
    </svg>
  </div>
  <ul class="contact-list">
    <li><span>addr</span>Elm Street 45, 1020 Springfield, USA</li>
    <li><span>tel</span>555/014-2290</li>
    <li><span>mail</span>daniel@halecounselingllc.com</li>
    <li><span>web</span>www.halecounselingllc.com</li>
  </ul>
</section>

</body>
</html>
```